One Page flat design for Car Classified Site

I'm looking for a flat design that that is very simple on the eye but with style. I need it to have a footer for some links etc, and the header needs a new feel but nothing to major.
This one page design is needed for the main page of the classified site...after this page is correct then all the other pages need to be designed to follow a similar style (new work).
I want more emphasis on the text rather than the images as a lot of users don't add images of the vehicles.
Attached is a mock up of the information and rough layout.
Wheelmarketlane.com is a classified site for car dealers only, I've also attached how the main competitions site looks.
Target Market(s)
Middle aged men, these guys are car dealers so it needs to be basic and easy for them as they aren't techie types.
Industry/Entity Type
Work
Number of Pages Required
1 page
Font styles to use
Look and feel

```html
<!DOCTYPE html>
<html lang="en">
<head>
<meta charset="utf-8">
<title>Wheelmarketlane – Search Results</title>
<link href="https://fonts.googleapis.com/css2?family=Open+Sans:wght@300;400;600&display=swap" rel="stylesheet">
<style>
  :root {
    --brand-blue: #1565b0;
    --title-blue: #1e6ab4;
    --page-grey: #efefef;
    --card-grey: #f4f4f4;
    --card-border: #cfcfcf;
    --field-border: #d6d6d6;
    --ink: #222222;
    --muted: #666666;
    --placeholder: #9a9a9a;
    --button-dark: #333333;
    --white: #ffffff;
  }
  * { box-sizing: border-box; margin: 0; padding: 0; }
  html, body { width: 1050px; height: 1200px; overflow: hidden; }
  body {
    position: relative;
    background: var(--page-grey);
    font-family: "Open Sans", sans-serif;
    color: var(--ink);
  }
  .hero-photo {
    position: absolute; left: 0; top: 0; width: 1050px; height: 324px;
    background: linear-gradient(180deg, #6f7479 0%, #3b3f44 55%, #26292c 100%);
  }
  .page-panel {
    position: absolute; left: 149px; top: 0; width: 751px; height: 1160px;
  }
  .top-bar {
    position: absolute; left: 0; top: 0; width: 751px; height: 41px;
    background: var(--white);
  }
  .login-label { position: absolute; left: 293px; top: 15px; font-size: 10px; color: var(--ink); }
  .login-field {
    position: absolute; top: 14px; height: 18px; width: 172px;
    border: 1px solid var(--field-border); background: #fafafa;
    font-size: 9px; color: #bbbbbb; padding: 3px 10px; font-weight: 300;
  }
  .login-field.username { left: 350px; }
  .login-field.password { left: 530px; }
  .login-link { position: absolute; left: 711px; top: 15px; font-size: 10px; color: var(--brand-blue); }
  .nav-bar {
    position: absolute; left: 0; top: 41px; width: 751px; height: 37px;
    background: var(--brand-blue); color: var(--white);
  }
  .brand-name { position: absolute; left: 14px; top: 3px; font-size: 26px; font-weight: 400; color: var(--white); }
  .nav-links { position: absolute; right: 10px; top: 12px; display: flex; gap: 12px; font-size: 10px; }
  .search-panel {
    position: absolute; left: 0; top: 103px; width: 751px; height: 1057px;
    background: var(--white);
  }
  .search-field {
    position: absolute; width: 352px; height: 35px;
    border: 1px solid var(--field-border); background: var(--white);
    font-size: 12px; font-style: italic; font-weight: 300; color: var(--placeholder);
    padding: 9px 10px;
  }
  .search-field svg { position: absolute; right: 10px; top: 13px; }
  .col-left { left: 11px; } .col-right { left: 392px; }
  .row-1 { top: 31px; } .row-2 { top: 86px; } .row-3 { top: 143px; }
  .advanced-search {
    position: absolute; left: 621px; top: 187px; width: 110px; height: 32px;
    background: var(--button-dark); color: #e6e6e6; font-size: 12px; font-style: italic; font-weight: 300;
    text-align: center; line-height: 32px;
  }
  .results-heading { position: absolute; left: 6px; top: 225px; font-size: 20px; font-weight: 400; }
  .listing {
    position: absolute; left: 5px; width: 741px; height: 231px;
    background: var(--card-grey); border: 1px solid var(--card-border);
  }
  .listing-title { position: absolute; left: 16px; top: 7px; font-size: 20px; font-weight: 400; color: var(--title-blue); }
  .listing-offer { position: absolute; right: 4px; top: 12px; font-size: 12px; color: var(--ink); }
  .photo-slot {
    position: absolute; left: 23px; top: 52px; width: 110px; height: 86px;
    border: 2px solid #bdbdbd; background: var(--white);
    font-size: 11px; color: #bbbbbb; text-align: center; line-height: 82px; font-weight: 300;
  }
  .vehicle-specs, .dealer-info { position: absolute; top: 56px; font-size: 12px; line-height: 18px; font-weight: 400; }
  .vehicle-specs { left: 153px; }
  .dealer-info { left: 296px; top: 50px; }
  .price-box {
    position: absolute; left: 520px; top: 47px; width: 201px; height: 69px;
    background: var(--brand-blue); color: var(--white); padding: 8px 18px; font-size: 12px;
  }
  .price-box h3 { font-size: 12px; font-weight: 600; margin-bottom: 1px; }
  .price-columns { display: flex; justify-content: space-between; line-height: 17px; font-weight: 300; }
  .dealer-comments { position: absolute; left: 24px; top: 151px; width: 700px; }
  .dealer-comments h4 { font-size: 12px; font-weight: 400; }
  .dealer-comments p { font-size: 9px; line-height: 13px; color: var(--muted); font-weight: 400; }
  .more-info {
    position: absolute; left: 587px; top: 194px; width: 99px; height: 26px;
    background: var(--brand-blue); color: var(--white); font-size: 13px; text-align: center; line-height: 26px;
  }
  .site-footer {
    position: absolute; left: 0; top: 1162px; width: 1050px; height: 38px;
    background: var(--white); display: flex; justify-content: center; gap: 14px;
    padding-top: 14px; font-size: 10px; color: var(--brand-blue);
  }
</style>
</head>
<body>
  <div class="hero-photo" role="img" aria-label="Photo of parked sports cars on tarmac"></div>

  <div class="page-panel">
    <header class="top-bar">
      <span class="login-label">Login Here</span>
      <div class="login-field username">Enter Username</div>
      <div class="login-field password">Enter Password</div>
      <span class="login-link">LOGIN</span>
    </header>
    <nav class="nav-bar">
      <span class="brand-name">Wheelmarketlane</span>
      <div class="nav-links"><span>Home</span><span>About us</span><span>Watch list</span></div>
    </nav>

    <main class="search-panel">
      <div class="search-field col-left row-1">Enter Make<svg width="8" height="7"><path d="M0 0H8L4 7Z" fill="#111"/></svg></div>
      <div class="search-field col-right row-1">Enter Model<svg width="8" height="7"><path d="M0 0H8L4 7Z" fill="#111"/></svg></div>
      <div class="search-field col-left row-2">Enter Price<svg width="8" height="7"><path d="M0 0H8L4 7Z" fill="#111"/></svg></div>
      <div class="search-field col-right row-2">Enter Age<svg width="8" height="7"><path d="M0 0H8L4 7Z" fill="#111"/></svg></div>
      <div class="search-field col-left row-3">Enter Body type<svg width="8" height="7"><path d="M0 0H8L4 7Z" fill="#111"/></svg></div>
      <div class="search-field col-right row-3">Enter a keyword<svg width="8" height="7"><path d="M0 0H8L4 7Z" fill="#111"/></svg></div>
      <div class="advanced-search">Advance Search</div>

      <h2 class="results-heading">Search Results listed below:</h2>

      <article class="listing" style="top:270px;">
        <h2 class="listing-title">2013 NORVAN ASHDALE TERRA VTX</h2>
        <span class="listing-offer">Buy it for $13570 or Please a Bid</span>
        <div class="photo-slot">image</div>
        <div class="vehicle-specs">2014<br>96000 Miles<br>Automatic<br>Black</div>
        <div class="dealer-info">Fenwick Motors UK<br>127 Miles Away</div>
        <div class="price-box"><h3>Trying to deal my customer</h3>
          <div class="price-columns"><span>Trade Price<br>$14,500</span><span>Retail Price<br>$16,900</span></div></div>
        <div class="dealer-comments"><h4>Dealer Comments:</h4>
          <p>Prepared for retail, Norvan GB plus 1 private owner, serviced twice at Norva&nbsp; at 7k and 18k-- 2keys available. Not yet due an MOT Prepared for retail, Norvan GB plus 1 private owner, serviced twice at Norva&nbsp; at 7k and 18k-- 2keys available. Not yet due an MOT</p></div>
        <div class="more-info">More Info</div>
      </article>

      <article class="listing" style="top:519px;">
        <h2 class="listing-title">2013 NORVAN ASHDALE TERRA VTX</h2>
        <span class="listing-offer">Buy it for $13570 or Please a Bid</span>
        <div class="photo-slot">image</div>
        <div class="vehicle-specs">2014<br>96000 Miles<br>Automatic<br>Black</div>
        <div class="dealer-info">Fenwick Motors UK<br>127 Miles Away</div>
        <div class="price-box"><h3>Trying to deal my customer</h3>
          <div class="price-columns"><span>Trade Price<br>$14,500</span><span>Retail Price<br>$16,900</span></div></div>
        <div class="dealer-comments"><h4>Dealer Comments:</h4>
          <p>Prepared for retail, Norvan GB plus 1 private owner, serviced twice at Norva&nbsp; at 7k and 18k-- 2keys available. Not yet due an MOT Prepared for retail, Norvan GB plus 1 private owner, serviced twice at Norva&nbsp; at 7k and 18k-- 2keys available. Not yet due an MOT</p></div>
        <div class="more-info">More Info</div>
      </article>

      <article class="listing" style="top:766px;">
        <h2 class="listing-title">2013 NORVAN ASHDALE TERRA VTX</h2>
        <span class="listing-offer">Buy it for $13570 or Please a Bid</span>
        <div class="photo-slot">image</div>
        <div class="vehicle-specs">2014<br>96000 Miles<br>Automatic<br>Black</div>
        <div class="dealer-info">Fenwick Motors UK<br>127 Miles Away</div>
        <div class="price-box"><h3>Trying to deal my customer</h3>
          <div class="price-columns"><span>Trade Price<br>$14,500</span><span>Retail Price<br>$16,900</span></div></div>
        <div class="dealer-comments"><h4>Dealer Comments:</h4>
          <p>Prepared for retail, Norvan GB plus 1 private owner, serviced twice at Norva&nbsp; at 7k and 18k-- 2keys available. Not yet due an MOT Prepared for retail, Norvan GB plus 1 private owner, serviced twice at Norva&nbsp; at 7k and 18k-- 2keys available. Not yet due an MOT</p></div>
        <div class="more-info">More Info</div>
      </article>
    </main>
  </div>

  <footer class="site-footer">
    <span>Contact us</span><span>About us</span><span>Legal info</span><span>Privacy Policy</span><span>Terms &amp; Conditions</span>
  </footer>
</body>
</html>
```